A small boutique Accounting and Mortgage Broking firm needs a business card design

Quorvel is a Brisbane based boutique accounting and mortgage broking firm. We offer a range of extensive financial services like accounting, tax consulting, book-keeping and mortgage broking.
We need a business card that stands out. The content can stay as it is on the existing card unless you recommend us to change anything on it for a better design.
Please remove the mobile number and give us a suitable format to change the details like email address and name.
Industry/Entity Type
Business
Contact Information for Business Card
Dalian Okoruwe
Quorvel Group Pty Ltd
3/412 Brackwin Rd Salisbury QLD 4107
PO Box 829 Salisbury QLD 4107
T 07 3184 5526
F 07 3952 1087
E dokoruwe@quorvel.net.au
Accountants Tax Agents, Mortgage Brokers
www.quorvel.net.au
Look and feel
Each slider illustrates characteristics of the customer's brand and the style your logo design should communicate.

```html
<!DOCTYPE html>
<html lang="en">
<head>
<meta charset="utf-8">
<title>Quorvel Business Card</title>
<link href="https://fonts.googleapis.com/css2?family=Open+Sans:wght@400;600;700&family=Oswald:wght@500;600&family=Raleway:wght@400&display=swap" rel="stylesheet">
<style>
  :root {
    --backdrop: #2b2b2f;
    --paper: #ffffff;
    --ink: #2f2f31;
    --charcoal: #2a2a2c;
    --grey: #4a4a4c;
    --green: #7dc243;
    --white: #ffffff;
  }
  * { margin: 0; padding: 0; box-sizing: border-box; }
  html, body {
    width: 1200px; height: 1000px; overflow: hidden;
    background: var(--backdrop);
  }
  .canvas {
    width: 1200px; height: 1000px;
    display: flex; flex-direction: column; align-items: center; justify-content: center;
    gap: 60px;
  }
  .card {
    position: relative;
    width: 700px; height: 400px;
    background: var(--paper);
    overflow: hidden;
    box-shadow: 0 10px 30px rgba(0,0,0,0.45);
  }

  /* Brand lockup */
  .brand { display: flex; align-items: center; gap: 10px; }
  .brand-dot { border-radius: 50%; border: 6px solid var(--grey); }
  .brand-name {
    font-family: "Open Sans", sans-serif; font-weight: 700; color: var(--grey);
  }

  /* Contact side */
  .contact .brand { position: absolute; top: 40px; right: 44px; }
  .contact .brand-dot { width: 54px; height: 54px; }
  .contact .brand-name { font-size: 30px; }
  .contact .rule {
    position: absolute; left: 250px; right: 48px; top: 140px;
    height: 2px; background: var(--green);
  }
  .contact .name {
    position: absolute; left: 40px; top: 128px;
    font-family: "Open Sans", sans-serif; font-weight: 600; font-size: 22px; color: var(--ink);
  }
  .contact .company {
    position: absolute; right: 48px; top: 158px; text-align: right;
    font-family: "Open Sans", sans-serif; font-style: normal;
    color: var(--ink); font-size: 14px; line-height: 1.45;
  }
  .contact .company strong { font-weight: 600; font-size: 15px; }
  .contact .details {
    position: absolute; left: 40px; top: 186px;
    list-style: none;
    font-family: "Open Sans", sans-serif; font-size: 16px; color: var(--ink); line-height: 1.5;
  }
  .contact .details li { display: flex; align-items: center; gap: 10px; }
  .contact .details svg { width: 14px; height: 14px; fill: var(--green); flex: none; }
  .contact .band { position: absolute; left: 0; top: 0; width: 700px; height: 400px; }
  .contact .web {
    position: absolute; right: 48px; top: 304px;
    font-family: "Open Sans", sans-serif; font-size: 15px; color: var(--white); letter-spacing: 0.5px;
  }

  /* Brand side */
  .front .brand { position: absolute; top: 56px; left: 0; right: 0; justify-content: center; gap: 14px; }
  .front .brand-dot { width: 86px; height: 86px; border-width: 9px; }
  .front .brand-name { font-size: 64px; letter-spacing: -1px; }
  .front .tagline {
    position: absolute; top: 160px; left: 0; right: 0; text-align: center;
    font-family: "Raleway", sans-serif; font-size: 34px; color: var(--grey); letter-spacing: 1px;
  }
  .front .services {
    position: absolute; top: 218px; left: 0; right: 0; height: 58px;
    background: var(--green);
    display: flex; align-items: center; justify-content: center; gap: 12px;
    font-family: "Oswald", sans-serif; font-weight: 600; font-size: 30px; color: var(--ink);
    text-transform: uppercase; letter-spacing: 0.5px;
  }
  .front .services .sep { width: 9px; height: 9px; border-radius: 50%; background: var(--white); }
  .front .web {
    position: absolute; top: 300px; left: 0; right: 0; text-align: center;
    font-family: "Oswald", sans-serif; font-weight: 500; font-size: 20px; color: var(--ink);
    letter-spacing: 1px;
  }
</style>
</head>
<body>
<main class="canvas">

  <section class="card contact">
    <svg class="band" viewBox="0 0 700 400" aria-hidden="true">
      <path d="M0 330 H400 C418 330 420 282 440 282 H700 V292 H446 C428 292 426 340 404 340 H0 Z" fill="var(--green)"/>
      <path d="M0 346 H408 C430 346 432 296 452 296 H700 V400 H0 Z" fill="var(--charcoal)"/>
    </svg>
    <div class="brand">
      <span class="brand-dot"></span>
      <span class="brand-name">Quorvel</span>
    </div>
    <div class="rule"></div>
    <h1 class="name">Dalian Okoruwe</h1>
    <address class="company">
      <strong>Quorvel Group Pty Ltd</strong><br>
      3/412 Brackwin Rd Carrowby QLD 4122<br>
      PO Box 829 Carrowby QLD 4122
    </address>
    <ul class="details">
      <li><svg viewBox="0 0 14 14"><path d="M3 1h4a1 1 0 0 1 1 1v10a1 1 0 0 1-1 1H3a1 1 0 0 1-1-1V2a1 1 0 0 1 1-1zm0 2v6h4V3z"/></svg>07 3184 5526</li>
      <li><svg viewBox="0 0 14 14"><path d="M3 1h7v4H3zM1 6h12v6h-2v-2H3v2H1zm3 5h6v2H4z"/></svg>07 3952 1087</li>
      <li><svg viewBox="0 0 14 14"><path d="M1 3h12v8H1zm1 1v.5l5 3.5 5-3.5V4z"/></svg>dokoruwe@quorvel.net.au</li>
    </ul>
    <div class="web">www.quorvel.net.au</div>
  </section>

  <section class="card front">
    <div class="brand">
      <span class="brand-dot"></span>
      <span class="brand-name">Quorvel</span>
    </div>
    <p class="tagline">CLEAR. FAIR. FORWARD.</p>
    <div class="services">
      <span>Accountants</span><span class="sep"></span>
      <span>Tax Agents</span><span class="sep"></span>
      <span>Mortgage Brokers</span>
    </div>
    <p class="web">WWW.QUORVEL.NET.RU</p>
  </section>

</main>
</body>
</html>
```